Iron Hoop Court Academy- Small Group and Private Lessons

I would like to advertise and drive my small group basketball lessons (offered on Fridays during the summer in Prosper, Texas with the following four groups- 1. Middle School Girls Small Group, 2. Middle School Boys Small Group, 3. High School Girls Small Group, 4. High School Boys Small Group).
Tag Line- "Do you want to become a complete player?"
We work to make each player as well rounded as possible by focusing on: balanced footwork, ballhandling, dribbling, finishing, passing, shooting, moving without the ball, basketball IQ
Website- www.ironhoopcourtacademy.com

```html
<!DOCTYPE html>
<html lang="en">
<head>
<meta charset="utf-8">
<title>Iron Hoop Court Academy – Small Group Lessons</title>
<link href="https://fonts.googleapis.com/css2?family=Anton&family=Oswald:wght@600;700&family=Lato:wght@400;700&display=swap" rel="stylesheet">
<style>
  :root {
    --orange: #ff8200;
    --orange-light: #ffa12a;
    --orange-dark: #e86f00;
    --black: #161616;
    --white: #ffffff;
    --page: #e9e7e4;
  }
  * { margin: 0; padding: 0; box-sizing: border-box; }
  html, body { width: 1200px; height: 1200px; overflow: hidden; background: var(--page); }
  .poster {
    position: absolute; left: 190px; top: 20px;
    width: 820px; height: 1160px; overflow: hidden;
    background: linear-gradient(160deg, var(--orange-light) 0%, var(--orange) 45%, var(--orange) 100%);
    font-family: "Lato", sans-serif;
  }
  .brand {
    position: absolute; left: 40px; top: 60px; width: 240px;
    display: flex; align-items: center; gap: 12px;
  }
  .brand-dot { width: 40px; height: 40px; border-radius: 50%; background: var(--black); flex: none; }
  .brand-name {
    font-family: "Oswald", sans-serif; font-weight: 700; font-size: 30px;
    line-height: 1.05; color: var(--black); text-transform: uppercase;
  }
  .headline {
    position: absolute; left: 295px; top: 30px; color: var(--black);
    font-family: "Anton", sans-serif; line-height: 1.1; font-weight: 400;
  }
  .headline .lead { font-size: 46px; display: block; }
  .headline .main { font-size: 60px; display: block; text-transform: uppercase; }
  .box { position: absolute; background: var(--black); color: var(--white); right: 0; }
  .band {
    position: absolute; right: 0; background: var(--orange-dark); color: var(--white);
    font-family: "Oswald", sans-serif; font-weight: 600; white-space: nowrap;
    box-shadow: 0 4px 8px rgba(0,0,0,.25);
  }
  .intro { left: 430px; top: 170px; height: 82px; padding: 14px 20px; font-size: 25px; line-height: 1.25; }
  .groups-title { left: 380px; top: 256px; height: 44px; padding: 7px 26px; font-size: 22px; }
  .groups { left: 450px; top: 300px; height: 158px; padding: 12px 22px; list-style: none; }
  .groups li { font-size: 20px; font-weight: 700; line-height: 36px; }
  .groups .num { color: var(--orange); margin-right: 4px; }
  .focus-title { left: 420px; top: 462px; height: 72px; padding: 6px 24px; font-size: 23px; line-height: 1.2; }
  .skills {
    left: 440px; top: 534px; height: 190px; padding: 20px 16px;
    display: grid; grid-template-columns: auto auto; column-gap: 24px;
  }
  .skills ul { list-style: none; }
  .skills li { font-size: 18px; line-height: 1.2; margin-bottom: 9px; display: flex; gap: 8px; white-space: nowrap; }
  .ball { width: 14px; height: 14px; flex: none; margin-top: 4px; }
  .player-photo {
    position: absolute; left: 40px; top: 210px; width: 330px; height: 830px;
    border-radius: 150px 150px 40px 40px;
    background: linear-gradient(180deg, #f4f4f6 0%, #d7d9e2 60%, #3a2a22 100%);
    opacity: .9;
  }
  .action-photo {
    position: absolute; width: 200px; height: 200px; border-radius: 50%;
    outline: 3px dashed var(--black); outline-offset: 6px;
  }
  .action-photo.court { left: 385px; top: 820px; background: radial-gradient(circle at 50% 40%, #f2e8e4, #a07a6c 70%, #6b4a40); }
  .action-photo.outdoor { left: 605px; top: 800px; background: radial-gradient(circle at 40% 35%, #bcd3f0, #5a86c6 70%, #3d5f93); }
  .footer {
    position: absolute; left: 0; bottom: 0; width: 100%; height: 95px;
    background: var(--black); display: flex; align-items: center; justify-content: center;
    font-size: 24px; color: var(--white);
  }
  .footer .site { color: var(--orange); text-transform: uppercase; }
</style>
</head>
<body>
<main class="poster">
  <div class="brand">
    <span class="brand-dot"></span>
    <span class="brand-name">Iron Hoop Court Academy</span>
  </div>

  <h1 class="headline">
    <span class="lead">Do you want to become a</span>
    <span class="main">Complete Player?</span>
  </h1>

  <div class="player-photo" role="img" aria-label="Basketball player in white uniform dribbling the ball"></div>

  <p class="box intro">offered on Fridays during the summer in Prosper</p>
  <h2 class="band groups-title">Texas with the following four groups</h2>
  <ol class="box groups">
    <li><span class="num">1.</span>Middle School Girls Small Group,</li>
    <li><span class="num">2.</span>Middle School Boys Small Group,</li>
    <li><span class="num">3</span> High School Girls Small Group,</li>
    <li><span class="num">4.</span>High School Boys Small Group</li>
  </ol>

  <h2 class="band focus-title">We work to make each player as well<br>rounded as possible by focusing on:</h2>
  <div class="box skills">
    <ul>
      <li><svg class="ball" viewBox="0 0 14 14"><circle cx="7" cy="7" r="6.5" fill="#ff8200"/><path d="M0.5 7h13M7 .5v13" stroke="#161616" stroke-width="1"/></svg>balanced footwork</li>
      <li><svg class="ball" viewBox="0 0 14 14"><circle cx="7" cy="7" r="6.5" fill="#ff8200"/><path d="M0.5 7h13M7 .5v13" stroke="#161616" stroke-width="1"/></svg>dribbling,</li>
      <li><svg class="ball" viewBox="0 0 14 14"><circle cx="7" cy="7" r="6.5" fill="#ff8200"/><path d="M0.5 7h13M7 .5v13" stroke="#161616" stroke-width="1"/></svg>passing</li>
      <li><svg class="ball" viewBox="0 0 14 14"><circle cx="7" cy="7" r="6.5" fill="#ff8200"/><path d="M0.5 7h13M7 .5v13" stroke="#161616" stroke-width="1"/></svg>moving without<br>the ball,</li>
    </ul>
    <ul>
      <li><svg class="ball" viewBox="0 0 14 14"><circle cx="7" cy="7" r="6.5" fill="#ff8200"/><path d="M0.5 7h13M7 .5v13" stroke="#161616" stroke-width="1"/></svg>ballhandling,</li>
      <li><svg class="ball" viewBox="0 0 14 14"><circle cx="7" cy="7" r="6.5" fill="#ff8200"/><path d="M0.5 7h13M7 .5v13" stroke="#161616" stroke-width="1"/></svg>finishing</li>
      <li><svg class="ball" viewBox="0 0 14 14"><circle cx="7" cy="7" r="6.5" fill="#ff8200"/><path d="M0.5 7h13M7 .5v13" stroke="#161616" stroke-width="1"/></svg>shooting</li>
      <li><svg class="ball" viewBox="0 0 14 14"><circle cx="7" cy="7" r="6.5" fill="#ff8200"/><path d="M0.5 7h13M7 .5v13" stroke="#161616" stroke-width="1"/></svg>basketball IQ</li>
    </ul>
  </div>

  <div class="action-photo court" role="img" aria-label="Girls basketball players reaching for a rebound in an indoor gym"></div>
  <div class="action-photo outdoor" role="img" aria-label="Player leaping toward an outdoor hoop against a blue sky"></div>

  <footer class="footer">www.<span class="site">ironhoopcourtacademy</span>.com</footer>
</main>
</body>
</html>
```